" Nós somos integradores de TI, nós fornecemos soluções de segurança e infraestrutura de TI para o mercado corporativo. Somos parceiros de empresas como Tarvok, Brix, Nuvexa, Quintorial entre outras. Nossos clientes são empresas e governos, mais especificamente os profissionais de TI destas empresas. "

```html
<!DOCTYPE html>
<html lang="pt-BR">
<head>
<meta charset="UTF-8">
<title>Datavel — A tecnologia muda o mundo</title>
<link rel="stylesheet" href="https://fonts.googleapis.com/css2?family=Roboto+Condensed:wght@400;700&display=swap">
<style>
  :root {
    --wood-dark: #5a3520;
    --wood-mid: #8a5a3b;
    --wood-light: #a97a58;
    --banner: #ffffff;
    --ink: #1c1c1c;
    --ink-soft: #333333;
  }
  * { margin: 0; padding: 0; box-sizing: border-box; }
  html, body {
    width: 1200px;
    height: 1200px;
    overflow: hidden;
  }
  body {
    position: relative;
    font-family: "Roboto Condensed", "Arial Narrow", sans-serif;
    color: var(--ink);
  }
  .wood-backdrop {
    position: absolute;
    inset: 0;
    background: linear-gradient(90deg,
      var(--wood-mid) 0%, var(--wood-light) 18%, var(--wood-mid) 36%,
      var(--wood-dark) 50%, var(--wood-light) 64%, var(--wood-mid) 82%,
      var(--wood-dark) 100%);
  }
  .banner {
    position: absolute;
    left: 84px;
    top: 365px;
    width: 1032px;
    height: 468px;
    background: var(--banner);
  }
  .brand {
    position: absolute;
    left: 60px;
    top: 200px;
    width: 312px;
    text-align: center;
  }
  .brand-name {
    font-weight: 400;
    font-size: 44px;
    line-height: 1;
    letter-spacing: 9px;
    color: var(--ink);
  }
  .brand-tagline {
    margin-top: 8px;
    font-weight: 400;
    font-size: 13px;
    letter-spacing: 2.2px;
    color: var(--ink-soft);
  }
  .message {
    position: absolute;
    left: 485px;
    top: 82px;
  }
  .headline {
    font-weight: 700;
    font-size: 73px;
    line-height: 74px;
    letter-spacing: 2px;
    color: var(--ink);
  }
  .subline {
    margin-top: 6px;
    font-weight: 400;
    font-size: 33px;
    line-height: 38px;
    letter-spacing: 0.5px;
    color: var(--ink-soft);
  }
</style>
</head>
<body>
  <div class="wood-backdrop" role="img" aria-label="Fundo de tábuas de madeira verticais em tons de marrom"></div>

  <section class="banner">
    <div class="brand">
      <p class="brand-name">DATAVEL</p>
      <p class="brand-tagline">TECNOLOGIA PARA NEGÓCIOS</p>
    </div>

    <div class="message">
      <h1 class="headline">A TECNOLOGIA<br>MUDA&nbsp; O<br>MUNDO</h1>
      <p class="subline">PESSOAS CRIAM<br>TECNOLOGIA</p>
    </div>
  </section>
</body>
</html>
```